Brannoch Tide mens beard oil and balm needs label design.

Brannoch Tide is a new Irish start up business that produces gentlemens grooming products. Our first two products will be beard oil and beard balm and we need label designs for both, there will be 3 beard oil products and 3 beard balm products, so label must be editable for ingrediants and product name.
We want the label to include a vintage/oldschool vibe with celtic influences that will appeal to both the older and younger gentleman.

Our bottles are 50ml blue circular glass bottles, dimensions are ht 92.2mm and diam of 37.22mm

Our tins are round aluminium screw on tins, dimensions are 70mm diam and 25mm ht.

label must have Made in Ireland.
Brannoch Tide must be prominent in labels.

winning designer will also get to design future products and other designs eg,stickers t shirt promotional material etc etc.

Ingrediants list can be provided when required.
Pictures of bottle and tin are attached.
Any questions feel free to ask.

Looking forward to seeing the designs.

Thanks
Brannoch Tide
Updates

Beard Oil ingrediants. Wanderfell Ingrediants- Peach Kernel(prunus persica), Grapeseed(vitis vinifera), Sweet almond(prunus dulcis), Golden Jojoba(simmondsia sinensis), Vitamin E. Essential oils- Grapefruit(citrus paradisi), Peppermint(mentha piperita) eucalyptus(eucalyptus globulas), Lime,cold pressed(citrus aurantifolia) Ironmark - Peach Kernel(prunus persica), Grapeseed(vitis vinifera), Sweet almond(prunus dulcis), Golden Jojoba(simmondsia sinensis), Vitamin E. Essential oils- sandalwood(amyris balsanifera), cedarwood(cedrus atlantica), Pine(pinus sylvestris) Overlord- Peach Kernel(prunus persica), Grapeseed(vitis vinifera), Sweet almond(prunus dulcis), Golden Jojoba(simmondsia sinensis), Vitamin E. Essential oils- ho leaf(cinnamomum camphora), Bay,west Indian(pimenta racemosa), Cinnamon leaf(cinnamomum zeylanium), Clove bud( eugenia caryophyllus) ps. ingrediants on balms(Tins) will follow. As for now use same ingrediants as above with inclusion of Shea butter, cocoa butter, natural beeswax Balms tins will keep the same pruducts names as beard oils(bottles) eg Wanderfell beard oil and Wanderfell beard balm. Thanks

Target Market(s)

Any man with a beard or mustache 18-80

Industry/Entity Type

Business

Requirements
Must have
• Made in Ireland
Handmade
room for barcode
room for 3 product name variations of both bottle and tin.
eg. Wanderfell, Ironmark, Dominion.

Wanderfell ingrediants- Peach Kernel(prunus persica), Grapeseed(vitis vinifera), Sweet almond(prunus dulcis), Golden Jojoba(simmondsia sinensis), Vitamin E.
Essential oils- Grapefruit(citrus paradisi), Peppermint(mentha piperita) eucalyptus(eucalyptus globulas), Lime,cold pressed(citrus aurantifolia)

Essential oil ingrediants which will change from product to product so must be editible from product to product
Nice to have
• Would be nice to see a Keltic design backround or outter edge.

```html
<!DOCTYPE html>
<html lang="en">
<head>
<meta charset="utf-8">
<title>Brannoch Tide – Wanderfell Label Set</title>
<link href="https://fonts.googleapis.com/css2?family=Oranienbaum&family=Sansita:wght@800&display=swap" rel="stylesheet">
<style>
  :root{
    --page:#ffffff;
    --panel:#333230;
    --panel-dark:#1d1916;
    --rim:#a3581f;
    --line:#cfcac2;
    --ink:#f1eee8;
    --ink-soft:#b9b5ae;
    --accent:#d71e26;
    --barcode-box:#ffffff;
    --label-font:"Oranienbaum", Georgia, serif;
    --name-font:"Sansita", "Arial Black", sans-serif;
  }
  html,body{margin:0;padding:0;overflow:hidden;background:var(--page);}
  .canvas{position:relative;width:1200px;height:1000px;overflow:hidden;background:var(--page);}
  .label{position:absolute;display:block;}
  .sprite{position:absolute;width:0;height:0;overflow:hidden;}
  .wrap-label{left:33px;top:5px;width:740px;height:300px;}
  .bottle-label{left:862px;top:190px;width:150px;height:150px;}
  .ingredients-lg{left:20px;top:350px;width:330px;height:330px;}
  .front-lg{left:400px;top:350px;width:330px;height:330px;}
  .ingredients-sm{left:80px;top:695px;width:220px;height:220px;}
  .front-sm{left:458px;top:695px;width:220px;height:220px;}
  .tin-lg{left:820px;top:365px;width:310px;height:310px;}
  .tin-sm{left:918px;top:705px;width:200px;height:200px;}
  .t-arc{font-family:var(--label-font);font-size:12px;fill:var(--ink);}
  .t-brand{font-family:var(--label-font);font-size:29px;fill:var(--ink);}
  .t-brand-lg{font-family:var(--label-font);font-size:34px;fill:var(--ink);}
  .t-product{font-family:var(--name-font);font-weight:800;fill:var(--accent);}
  .t-small{font-family:var(--label-font);font-size:9px;fill:var(--ink);}
  .t-body{font-family:var(--label-font);font-size:15px;fill:var(--ink);}
  .t-side{font-family:var(--label-font);font-size:17px;fill:var(--ink);}
  .t-head{font-family:var(--label-font);font-size:40px;fill:var(--ink-soft);}
  .t-upc{font-family:var(--label-font);font-size:20px;fill:#111;}
</style>
</head>
<body>
<div class="canvas">

<svg class="sprite" aria-hidden="true">
  <defs>
    <radialGradient id="portrait-fill" cx="50%" cy="45%" r="60%">
      <stop offset="0" stop-color="#e9e7e3"/>
      <stop offset="1" stop-color="#7a7874"/>
    </radialGradient>
    <path id="arc-top" d="M31,165 A134,134 0 0 1 299,165" fill="none"/>
    <path id="arc-bot" d="M24,165 A141,141 0 0 0 306,165" fill="none"/>
  </defs>

  <symbol id="label-frame" viewBox="0 0 330 330">
    <circle cx="165" cy="165" r="165" style="fill:var(--panel-dark)"/>
    <circle cx="165" cy="165" r="157" style="fill:none;stroke:var(--rim);stroke-width:6"/>
    <circle cx="165" cy="165" r="152" style="fill:var(--panel)"/>
    <circle cx="165" cy="165" r="146" style="fill:none;stroke:var(--line);stroke-width:0.8"/>
  </symbol>

  <symbol id="front-core" viewBox="0 0 330 330">
    <text class="t-brand" x="165" y="118" text-anchor="middle">Brannoch Tide</text>
    <g role="img" aria-label="Bearded man portrait emblem">
      <circle cx="165" cy="158" r="32" fill="url(#portrait-fill)" stroke="#111" stroke-width="3"/>
    </g>
    <text class="t-product" x="165" y="228" font-size="40" text-anchor="middle" transform="rotate(-9 165 215)">Wanderfell</text>
    <text class="t-small" x="165" y="292" text-anchor="middle">50ml</text>
    <text class="t-small" x="165" y="305" text-anchor="middle">Made in Ireland</text>
  </symbol>

  <symbol id="front-oil" viewBox="0 0 330 330">
    <use href="#label-frame"/>
    <text class="t-arc"><textPath href="#arc-top" startOffset="17%">Beard Oil</textPath></text>
    <text class="t-arc"><textPath href="#arc-top" startOffset="71%">Beard Oil</textPath></text>
    <text class="t-arc"><textPath href="#arc-bot" startOffset="24%">Beard Oil</textPath></text>
    <text class="t-arc"><textPath href="#arc-bot" startOffset="64%">Beard Oil</textPath></text>
    <use href="#front-core"/>
  </symbol>

  <symbol id="front-balm" viewBox="0 0 330 330">
    <use href="#label-frame"/>
    <text class="t-arc"><textPath href="#arc-top" startOffset="16%">Beard Balm</textPath></text>
    <text class="t-arc"><textPath href="#arc-top" startOffset="70%">Beard Balm</textPath></text>
    <text class="t-arc"><textPath href="#arc-bot" startOffset="23%">Beard Balm</textPath></text>
    <text class="t-arc"><textPath href="#arc-bot" startOffset="63%">Beard Balm</textPath></text>
    <use href="#front-core"/>
  </symbol>

  <symbol id="ingredients" viewBox="0 0 330 330">
    <use href="#label-frame"/>
    <text class="t-brand-lg" x="165" y="102" text-anchor="middle">Brannoch Tide</text>
    <text class="t-product" x="165" y="138" font-size="32" text-anchor="middle" transform="rotate(-9 165 128)">Wanderfell</text>
    <text class="t-body" x="165" y="172" text-anchor="middle">Ingrediants</text>
    <text class="t-body" x="165" y="189" text-anchor="middle">Peach Kernel(prunus persica),</text>
    <text class="t-body" x="165" y="206" text-anchor="middle">Grapeseed(vitis vinifera), Sweet</text>
    <text class="t-body" x="165" y="223" text-anchor="middle">almond(prunus dulcis), Golden</text>
    <text class="t-body" x="165" y="240" text-anchor="middle">Jojoba(simmondsia sinensis),</text>
    <text class="t-body" x="165" y="257" text-anchor="middle">Vitamin E.</text>
    <text class="t-small" x="165" y="292" text-anchor="middle">50ml</text>
    <text class="t-small" x="165" y="305" text-anchor="middle">Made in Ireland</text>
  </symbol>
</svg>

<svg class="label wrap-label" viewBox="0 0 740 300" role="group" aria-label="Beard oil bottle wrap label">
  <rect width="740" height="300" style="fill:var(--panel)"/>
  <rect x="31" y="38" width="98" height="227" style="fill:var(--barcode-box)"/>
  <text class="t-upc" transform="translate(73 151) rotate(90)" text-anchor="middle">UPC Code</text>
  <text class="t-side" transform="translate(168 151) rotate(90)" text-anchor="middle">Company info</text>
  <text class="t-side" transform="translate(146 151) rotate(90)" text-anchor="middle">website</text>
  <use href="#front-oil" x="237" y="14" width="270" height="270"/>
  <text class="t-head" transform="translate(562 262) rotate(-90)">Essential oil</text>
  <text class="t-side" transform="translate(592 150) rotate(-90)" text-anchor="middle">Ingrediants</text>
  <text class="t-side" transform="translate(614 288) rotate(-90)">Grapefruit(citrus paradisi),</text>
  <text class="t-side" transform="translate(636 288) rotate(-90)">Peppermint(mentha piperita)</text>
  <text class="t-side" transform="translate(658 288) rotate(-90)">eucalyptus(eucalyptus globulas),</text>
  <text class="t-side" transform="translate(680 288) rotate(-90)">Lime,cold pressed(citrus aurantifolia)</text>
</svg>

<svg class="label bottle-label" viewBox="0 0 330 330" role="group" aria-label="Beard oil bottle front label"><use href="#front-oil"/></svg>
<svg class="label ingredients-lg" viewBox="0 0 330 330" role="group" aria-label="Large tin ingredients label"><use href="#ingredients"/></svg>
<svg class="label front-lg" viewBox="0 0 330 330" role="group" aria-label="Large tin lid label"><use href="#front-balm"/></svg>
<svg class="label ingredients-sm" viewBox="0 0 330 330" role="group" aria-label="Small tin ingredients label"><use href="#ingredients"/></svg>
<svg class="label front-sm" viewBox="0 0 330 330" role="group" aria-label="Small tin lid label"><use href="#front-balm"/></svg>
<svg class="label tin-lg" viewBox="0 0 330 330" role="group" aria-label="Large tin lid label"><use href="#front-balm"/></svg>
<svg class="label tin-sm" viewBox="0 0 330 330" role="group" aria-label="Small tin lid label"><use href="#front-balm"/></svg>

</div>
</body>
</html>
```